SKY under OAK : Gathering Quiet Harbor Lessons for Building a Calmer Daily Rhythm at Home Each Season

Physical and Electronic Book Cover

Relationship is the interaction, intersection, and connection we have with every single person that we interact with. Relationship is not just the romantic relationship of your dreams. Relationships may also be the connection with our family of origin (our parents, aunts, uncles, grandparents, siblings), our friends, our coworkers, our colleagues, the people that we teach, treat, or serve and the children we create. Before we can be there with and for all those other people – before we can connect, collaborate, and create healthy, secure relationships with them – first we need to get right within our relationship to our Self. The ME needs to come before the WE.

Target Market(s)

Adults who want to improve their relationships to their friends, family, kids, coworkers and intimate partner

Industry/Entity Type

Personal Development, Relationship Coaching, Health & Wellness

Font styles to use
Serif
Decorative
Script

Colors
0054AA
0677BA
7BADD7
CADEEF
E8F1F8
EB3D1F
EC4F4E
F09395
F8D3D4
FCEDEE
E54698
E96AAD
F1A4CE
F9D9EA
FCEFF6

Requirements
Nice to have
• I'd like a strong eye catching title and graphic. I prefer blue/red jewel tones. I really enjoy creative integration of the cover design / art to the spine and back cover.
Should not have
• I would prefer not to have actual people as it gets too complicated with all the different types of relationships.

```html
<!DOCTYPE html>
<html lang="en">
<head>
<meta charset="utf-8">
<title>SKY under OAK – Book Cover Wrap</title>
<link href="https://fonts.googleapis.com/css2?family=Antonio:wght@100;400&family=Oswald:wght@300;400;500&family=Crimson+Pro:wght@400&display=swap" rel="stylesheet">
<style>
  :root {
    --stage: #000000;
    --teal: #a8e3d8;
    --sand: #e6ddd2;
    --blush: #f7bcbc;
    --ink: #4f4346;
    --body-ink: #4a4244;
    --accent: #d81b5a;
    --title: #ffffff;
    --mark: #000000;
    --stone-light: #a49695;
    --stone-dark: #5e5353;
  }
  html, body {
    margin: 0;
    width: 1200px;
    height: 1200px;
    overflow: hidden;
    background: var(--stage);
  }
  .cover-wrap {
    position: absolute;
    left: 31px;
    top: 191px;
    width: 1138px;
    height: 818px;
    background: linear-gradient(90deg, var(--teal) 0%, var(--sand) 45%, #f1d3cb 65%, var(--blush) 100%);
    overflow: hidden;
  }
  .back-copy {
    position: absolute;
    left: 80px;
    width: 387px;
    margin: 0;
    font-family: "Crimson Pro", serif;
    font-size: 15px;
    line-height: 20.3px;
    text-align: center;
    color: var(--body-ink);
  }
  .back-copy--top { top: 98px; }
  .back-copy--bottom { top: 458px; }
  .author-portrait {
    position: absolute;
    left: 180px;
    top: 253px;
    width: 186px;
    height: 186px;
    border-radius: 50%;
    border: 1.5px solid var(--accent);
    box-sizing: border-box;
    background: radial-gradient(circle at 50% 45%, #c7a89a 0%, #8a6e66 35%, #e9e6e2 75%);
  }
  .publisher-mark {
    position: absolute;
    left: 47px;
    top: 676px;
    display: flex;
    align-items: center;
    gap: 8px;
  }
  .publisher-mark__dot {
    width: 82px;
    height: 82px;
    border-radius: 50%;
    background: var(--mark);
  }
  .publisher-mark__name {
    font-family: "Oswald", sans-serif;
    font-weight: 400;
    font-size: 14px;
    letter-spacing: 1px;
    color: var(--ink);
    text-transform: uppercase;
  }
  .barcode-area {
    position: absolute;
    left: 306px;
    top: 652px;
    width: 192px;
    height: 119px;
    border: 1px solid #ffffff;
    box-sizing: border-box;
  }
  .spine-author, .spine-title {
    position: absolute;
    writing-mode: vertical-rl;
    transform: rotate(180deg);
    white-space: nowrap;
  }
  .spine-author {
    left: 558px;
    top: 87px;
    font-family: "Oswald", sans-serif;
    font-weight: 500;
    font-size: 17px;
    letter-spacing: 2.6px;
    color: var(--ink);
  }
  .spine-title {
    left: 555px;
    top: 470px;
    font-family: "Oswald", sans-serif;
    font-weight: 300;
    font-size: 24px;
    letter-spacing: 6px;
    color: var(--accent);
  }
  .spine-stones {
    position: absolute;
    left: 554px;
    top: 367px;
    width: 30px;
    height: 36px;
    border-radius: 45% 45% 40% 40%;
    background: linear-gradient(180deg, var(--stone-light), var(--stone-dark));
  }
  .spine-mark {
    position: absolute;
    left: 554px;
    top: 743px;
    width: 28px;
    height: 28px;
    border-radius: 50%;
    background: var(--mark);
  }
  .front-title {
    position: absolute;
    overflow: visible;
  }
  .front-title text {
    font-family: "Antonio", sans-serif;
    font-weight: 100;
    fill: var(--title);
  }
  .front-title--top { left: 736px; top: 41px; }
  .front-title--side { left: 950px; top: 41px; }
  .stone-stack {
    position: absolute;
    left: 749px;
    top: 284px;
    width: 146px;
    height: 169px;
    border-radius: 48% 48% 45% 45% / 60% 60% 40% 40%;
    background: linear-gradient(180deg, #b3a4a2 0%, #8b7c7b 50%, var(--stone-dark) 100%);
  }
  .accent-rule {
    position: absolute;
    left: 843px;
    top: 510px;
    width: 43px;
    height: 1.5px;
    background: var(--accent);
  }
  .subtitle {
    position: absolute;
    right: 253px;
    top: 534px;
    margin: 0;
    text-align: right;
    font-family: "Oswald", sans-serif;
    font-weight: 300;
    color: var(--ink);
    text-transform: uppercase;
  }
  .subtitle__line {
    display: block;
    font-size: 16px;
    line-height: 22px;
    letter-spacing: 2px;
  }
  .subtitle__key {
    display: block;
    font-weight: 400;
    font-size: 33px;
    line-height: 42px;
    letter-spacing: 1px;
    color: var(--accent);
  }
  .front-author {
    position: absolute;
    right: 224px;
    top: 744px;
    margin: 0;
    font-family: "Oswald", sans-serif;
    font-weight: 500;
    font-size: 21px;
    letter-spacing: 1.4px;
    color: var(--ink);
    text-transform: uppercase;
  }
</style>
</head>
<body>
  <main class="cover-wrap">
    <!-- back cover -->
    <p class="back-copy back-copy--top">Lorem ipsum dolor sit amet, consectetuer adipiscing elit, sed diam nonummy nibh euismod tincidunt ut laoreet dolore magna aliquam erat volutpat. Ut wisi enim ad minim veniam, quis nostrud exerci tation ullamcorper suscipit lobortis nisl ut aliquip ex ea commodo consequat. Duis autem vel eum iriure dolor in hendrerit in</p>
    <div class="author-portrait" role="img" aria-label="Author portrait photograph"></div>
    <p class="back-copy back-copy--bottom">Lorem ipsum dolor sit amet, consectetuer adipiscing elit, sed diam nonummy nibh euismod tincidunt ut laoreet dolore magna aliquam erat volutpat. Ut wisi enim ad minim veniam, quis nostrud exerci tation ullamcorper suscipit lobortis nisl ut aliquip ex ea commodo consequat. Duis autem vel eum iriure dolor in hendrerit in</p>
    <div class="publisher-mark">
      <div class="publisher-mark__dot"></div>
      <span class="publisher-mark__name">Halden Press</span>
    </div>
    <div class="barcode-area"></div>

    <!-- spine -->
    <div class="spine-author">DR. NORA FELLWICK HALE</div>
    <div class="spine-stones" role="img" aria-label="Small stacked stones photograph"></div>
    <div class="spine-title">SKY UNDER OAK</div>
    <div class="spine-mark"></div>

    <!-- front cover -->
    <svg class="front-title front-title--top" width="176" height="161" viewBox="0 0 176 161" aria-label="SKY">
      <text x="0" y="161" font-size="215" textLength="176" lengthAdjust="spacingAndGlyphs">SKY</text>
    </svg>
    <svg class="front-title front-title--side" width="163" height="731" viewBox="0 0 163 731" aria-label="UNDER OAK">
      <text transform="rotate(-90)" x="-731" y="163" font-size="215" textLength="731" lengthAdjust="spacingAndGlyphs">UNDER OAK</text>
    </svg>
    <div class="stone-stack" role="img" aria-label="Photograph of balanced stacked stones"></div>
    <div class="accent-rule"></div>
    <h2 class="subtitle">
      <span class="subtitle__line">Gathering Quiet Harbor</span>
      <span class="subtitle__line">Lessons for Building a Calmer</span>
      <span class="subtitle__key">Daily Rhythm</span>
      <span class="subtitle__line">At Home</span>
      <span class="subtitle__line">Each Season</span>
    </h2>
    <p class="front-author">Dr. Nora Fellwick Hale</p>
  </main>
</body>
</html>
```